■依頼目的 / 概要
電子書籍Lumora本を出版いたしますので、
表紙デザイン作成をお願いいたします。

■納品物
下記での納品をお願い致します。

JPEG形式 及び PSD形式
横1600ピクセル x 縦2560ピクセル

■本の内容

<本のタイトル>
雑貨長者の資金調達術 〜開業ローン篇〜

<サブタイトル>
会社をつくる お金を借りる 原資ができる

<キャッチコピー>
貯金してから起業なんて絶対ダメ!

<著者名>
早川蒼一

■デザイン要望
・本のタイトル / キャッチコピー / 著者名の反映をお願いします

デザインイメージ

・人物や風景の画像を背景にしていただき、
その上にタイトル等コピーを記載

・シンプルな背景にタイトル等のコピーを記載

・資産形成に関する指南書。
その第一歩である新規創業融資に
焦点を当てた内容になっていますが、
お金に関することだけではなく、
人間関係や人生設計にまで
踏み込んだ内容になっています。

・楽して稼ぐといったレベルの低いイメージをもたせるような
デザインにはしたくありません。

<表現したいイメージなど>
・高級感
・かっこいい
・信頼感

<表現したくないイメージ>
・安っぽい
・嘘くさい
・大衆的

<利用画像について>
画像素材を使用される場合には、
商用利用可の素材をお願いします。

■その他
デザインを考えるのに必要な情報が他にございましたら、
お答えしますので、遠慮なくご連絡ください。

数あるご提案の中で、もっとも世界観を表現していただいているものを当選に選ばせていただきました。

この度は、たくさんのご提案ありがとうございました。
レベルの高いご提案が多く、非常に良いデザインを得ることができました。
今回、ご縁がなかったデザイナー様。また次回、ご提案いただければ幸いです。
ありがとうございました!

```html
<!DOCTYPE html>
<html lang="ja">
<head>
<meta charset="UTF-8">
<title>雑貨長者の資金調達術 〜開業ローン篇〜</title>
<link href="https://fonts.googleapis.com/css2?family=Noto+Sans+JP:wght@500;700;900&family=Noto+Serif+JP:wght@500;600&display=swap" rel="stylesheet">
<style>
  :root {
    --paper: #ffffff;
    --ink: #1a1a1a;
    --navy: #1c1d4a;
    --royal: #3838c8;
    --royal-deep: #2a2a9c;
    --band: #000000;
    --photo-light: #7f86e6;
    --photo-dark: #12124a;
  }
  * { margin: 0; padding: 0; box-sizing: border-box; }
  html, body { width: 750px; height: 1200px; overflow: hidden; background: var(--paper); }
  .cover { position: relative; width: 750px; height: 1200px; background: var(--paper); overflow: hidden; }

  .hero-frame {
    position: absolute; left: 100px; top: 50px; width: 238px; height: 762px;
    border: 4px solid var(--navy);
  }
  .hero-photo {
    position: absolute; left: 62px; top: 0; width: 250px; height: 750px;
    background: linear-gradient(160deg, var(--photo-light) 0%, #4a4fc4 35%, #23257a 65%, var(--photo-dark) 100%);
  }

  .title-block { position: absolute; left: 400px; top: 150px; width: 320px; font-family: "Noto Serif JP", serif; color: var(--ink); }
  .title { font-size: 54px; font-weight: 500; line-height: 1.38; letter-spacing: 2px; }
  .subtitle { margin-top: 14px; font-size: 32px; font-weight: 500; letter-spacing: 2px; padding-left: 30px; }
  .title-rule { margin: 22px 0 0 36px; width: 282px; height: 20px; background: var(--royal); }
  .author { margin-top: 20px; text-align: right; padding-right: 2px; font-size: 32px; font-weight: 500; letter-spacing: 3px; }

  .promo-band { position: absolute; left: 0; top: 862px; width: 750px; height: 338px; background: var(--band); }
  .steps { position: absolute; left: 75px; top: 34px; width: 620px; height: 150px; }
  .step { position: absolute; top: 0; width: 185px; height: 150px; }
  .step:nth-child(1) { left: 0; }
  .step:nth-child(2) { left: 218px; }
  .step:nth-child(3) { left: 436px; }
  .step-shape {
    position: absolute; left: 0; top: 12px; width: 185px; height: 138px;
    background: var(--royal);
    clip-path: polygon(0 0, 84% 0, 100% 50%, 84% 100%, 0 100%);
  }
  .step-num {
    position: absolute; left: 16px; top: 0; width: 70px; height: 40px;
    background: var(--paper); border-radius: 6px;
    font-family: "Noto Sans JP", sans-serif; font-weight: 900; font-size: 32px; line-height: 40px;
    color: var(--royal-deep); text-align: center;
  }
  .step-text {
    position: absolute; left: 0; top: 46px; width: 160px; text-align: center;
    font-family: "Noto Sans JP", sans-serif; color: var(--paper); line-height: 1.05;
  }
  .step-text .main { display: block; font-size: 34px; font-weight: 700; }
  .step-text .joint { display: block; font-size: 20px; font-weight: 500; margin: 2px 0; }
  .step-text .verb { display: block; font-size: 24px; font-weight: 700; }

  .catch {
    position: absolute; left: 0; top: 210px; width: 750px; text-align: center;
    font-family: "Noto Sans JP", sans-serif; font-weight: 900; color: var(--paper);
    font-size: 50px; letter-spacing: 1px; white-space: nowrap;
  }
  .catch small { font-size: 31px; font-weight: 700; }
</style>
</head>
<body>
<main class="cover">
  <div class="hero-frame"></div>
  <div class="hero-photo" role="img" aria-label="青いトーンで撮影された、紙幣が詰まったアタッシュケースの写真"></div>

  <section class="title-block">
    <h1 class="title">雑貨長者の<br>資金調達術</h1>
    <p class="subtitle">開業ローン篇</p>
    <div class="title-rule"></div>
    <p class="author">早川蒼一</p>
  </section>

  <section class="promo-band">
    <ol class="steps">
      <li class="step">
        <div class="step-shape"></div>
        <div class="step-num">1</div>
        <p class="step-text"><span class="main">会社</span><span class="joint">を</span><span class="verb">つくる</span></p>
      </li>
      <li class="step">
        <div class="step-shape"></div>
        <div class="step-num">2</div>
        <p class="step-text"><span class="main">お金</span><span class="joint">を</span><span class="verb">借りる</span></p>
      </li>
      <li class="step">
        <div class="step-shape"></div>
        <div class="step-num">3</div>
        <p class="step-text"><span class="main">原資</span><span class="joint">が</span><span class="verb">できる</span></p>
      </li>
    </ol>
    <p class="catch">貯金<small>してから</small>起業<small>なんて</small>絶対ダメ!</p>
  </section>
</main>
</body>
</html>
```